Invesment management business need a stationery design

We need a stationery design for a new company based in Sao Paulo, Brazil, called "Brixwell Capital". We provide investment management services for individuals and corporations.
The final design should communicate financial safety and some kind of luxury, just like an investment bank does.
As an inspiration, the designer could take a look at companies like KT Hollins, Fenwick Ardsley, RQT or Talbrook Vesse

Target Market(s)

Individuals and corporations

Industry/Entity Type

Business

Requirements
Must have
• My project must have our logo on it.
• Our business cards should have our contact information, such as telephone number and emails.

```html
<!DOCTYPE html>
<html lang="en">
<head>
<meta charset="utf-8">
<title>Brixwell Capital — Stationery</title>
<link href="https://fonts.googleapis.com/css2?family=Lato:wght@300;400;700&display=swap" rel="stylesheet">
<style>
  :root{
    --bg:#d9d9d9;
    --paper:#f7f7f7;
    --ink:#2b2b2b;
    --ink-soft:#6a6a6a;
    --black:#1f1d1e;
    --black-deep:#161415;
    --on-dark:#e4e4e4;
    --accent:#c9a24a;
    --accent-blue:#3c8fc6;
    --shadow:0 8px 18px rgba(0,0,0,.18);
  }
  *{box-sizing:border-box;margin:0;padding:0}
  html,body{width:1200px;height:1000px;overflow:hidden}
  body{background:var(--bg);font-family:"Lato",sans-serif;color:var(--ink);position:relative}

  .item{position:absolute;box-shadow:var(--shadow)}
  .paper{background:var(--paper)}
  .dark{background:var(--black)}

  /* brand */
  .brand{display:flex;align-items:center;gap:6px}
  .brand__dot{width:14px;height:14px;border-radius:50%;background:var(--accent)}
  .brand__name{font-family:"Lato",sans-serif;font-weight:400;letter-spacing:.12em;line-height:1.05;text-transform:uppercase;font-size:9px;color:var(--ink)}
  .brand--light .brand__name{color:var(--on-dark)}
  .brand--lg .brand__dot{width:34px;height:34px}
  .brand--lg .brand__name{font-size:20px;letter-spacing:.14em}
  .brand--lg{gap:12px}

  /* letterhead */
  .letterhead{left:150px;top:150px;width:275px;height:390px;padding:38px 30px 0}
  .letterhead .brand{justify-content:center;margin-bottom:42px}
  .letter{font-size:5.2px;line-height:1.7;color:var(--ink-soft)}
  .letter p{margin-bottom:8px}
  .letter__salute{color:var(--ink);font-size:6px;margin-bottom:10px!important}
  .letter__close{text-align:right;color:var(--ink);margin-top:14px}
  .letter__sign{text-align:right;color:var(--ink);font-size:6px;margin-top:14px}
  .contact-line{position:absolute;left:22px;right:22px;bottom:14px;border-top:1px solid var(--accent);padding-top:4px;font-size:3.6px;color:var(--ink-soft);letter-spacing:.03em;white-space:nowrap;overflow:hidden}
  .contact-line b{color:var(--accent-blue);font-weight:700}

  /* envelopes */
  .envelope-open{left:455px;top:150px;width:225px;height:190px;box-shadow:none}
  .envelope-open__flap{position:absolute;left:0;top:0;width:225px;height:72px;background:var(--black);border-radius:6px 6px 0 0;box-shadow:var(--shadow)}
  .envelope-open__flap .brand{position:absolute;right:12px;top:14px}
  .envelope-open__body{position:absolute;left:0;top:72px;width:225px;height:118px;background:var(--paper);box-shadow:var(--shadow)}
  .envelope-open__body svg{position:absolute;inset:0}

  .envelope-front{left:705px;top:150px;width:230px;height:118px}
  .envelope-front .brand{position:absolute;left:14px;bottom:26px}
  .envelope-front .contact-line{left:14px;right:14px;bottom:12px}

  .envelope-back{left:705px;top:290px;width:230px;height:118px;overflow:hidden}
  .envelope-back__flap{position:absolute;left:0;top:0;width:230px;height:54px;background:var(--black);border-radius:0 0 4px 4px}
  .envelope-back__flap .brand{position:absolute;left:50%;top:50%;transform:translate(-50%,-50%)}

  /* business cards */
  .card{width:112px;height:64px}
  .card--front{left:462px;top:392px;display:flex;align-items:center;justify-content:center}
  .card--back{left:592px;top:392px;padding:8px}
  .card__person{position:absolute;right:10px;top:20px;text-align:right;font-size:5px;color:var(--ink)}
  .card__person span{display:block;color:var(--ink-soft);font-size:3.8px;margin-top:1px}
  .card__contact{position:absolute;left:8px;bottom:7px;font-size:3.6px;line-height:1.5;color:var(--ink-soft)}
  .card__contact b{color:var(--accent-blue)}

  /* folder closed */
  .folder-cover{left:150px;top:560px;width:300px;height:405px;background:linear-gradient(160deg,#242223 0%,var(--black-deep) 100%);padding:60px 0 0 60px}

  /* folder open */
  .folder-open{left:480px;top:470px;width:580px;height:400px;display:flex;gap:2px;box-shadow:none}
  .folder-open__panel{position:relative;flex:1;background:var(--paper);box-shadow:var(--shadow)}
  .folder-open__pocket{position:absolute;left:0;right:0;bottom:0;height:150px;background:var(--black);border-radius:8px 8px 0 0}
  .folder-open__panel--right .folder-open__pocket{border-radius:8px 0 0 0}
  .folder-open__panel--right .brand{position:absolute;right:18px;top:18px}
  .folder-open__panel--left .folder-open__pocket{border-radius:0 22px 0 0}
</style>
</head>
<body>

  <!-- letterhead -->
  <article class="item paper letterhead">
    <div class="brand"><span class="brand__dot"></span><span class="brand__name">Brixwell<br>Capital</span></div>
    <div class="letter">
      <p class="letter__salute">Dear Client,</p>
      <p>We are pleased to confirm the opening of your portfolio with our firm. Our advisors have reviewed your goals and prepared a strategy built on discipline, diversification and long-term value.</p>
      <p>Enclosed you will find a summary of the proposed allocation, the applicable fees and the reporting calendar for the coming year.</p>
      <p>Please contact your relationship manager with any questions. We look forward to a lasting partnership.</p>
      <p class="letter__close">Best regards,</p>
      <p class="letter__sign">Lucas Moreau</p>
    </div>
    <div class="contact-line"><b>Address</b> Av. Paulista 1200, São Paulo &nbsp;|&nbsp; <b>Phone</b> +55 11 4000 2817 &nbsp;|&nbsp; <b>Email</b> info@brixwellcapital.com &nbsp;|&nbsp; <b>Web</b> www.brixwellcapital.com</div>
  </article>

  <!-- open envelope -->
  <div class="item envelope-open">
    <div class="envelope-open__flap">
      <div class="brand brand--light"><span class="brand__dot"></span><span class="brand__name">Brixwell<br>Capital</span></div>
    </div>
    <div class="envelope-open__body">
      <svg width="225" height="118" viewBox="0 0 225 118"><polyline points="0,0 22,34 203,34 225,0" fill="none" stroke="#d8d8d8" stroke-width="1"/></svg>
    </div>
  </div>

  <!-- envelope front -->
  <div class="item paper envelope-front">
    <div class="brand"><span class="brand__dot"></span><span class="brand__name">Brixwell<br>Capital</span></div>
    <div class="contact-line"><b>Address</b> Av. Paulista 1200, São Paulo &nbsp;|&nbsp; <b>Phone</b> +55 11 4000 2817 &nbsp;|&nbsp; <b>Email</b> info@brixwellcapital.com &nbsp;|&nbsp; <b>Web</b> www.brixwellcapital.com</div>
  </div>

  <!-- envelope back -->
  <div class="item paper envelope-back">
    <div class="envelope-back__flap">
      <div class="brand brand--light"><span class="brand__dot"></span><span class="brand__name">Brixwell<br>Capital</span></div>
    </div>
  </div>

  <!-- business cards -->
  <div class="item dark card card--front">
    <div class="brand brand--light"><span class="brand__dot"></span><span class="brand__name">Brixwell<br>Capital</span></div>
  </div>
  <div class="item paper card card--back">
    <div class="brand"><span class="brand__dot" style="width:9px;height:9px"></span><span class="brand__name" style="font-size:5.5px">Brixwell<br>Capital</span></div>
    <div class="card__person">Lucas Moreau<span>Managing Director</span></div>
    <div class="card__contact"><b>T</b> +55 11 4000 2817<br><b>E</b> l.moreau@brixwellcapital.com</div>
  </div>

  <!-- closed folder -->
  <div class="item folder-cover">
    <div class="brand brand--light brand--lg"><span class="brand__dot"></span><span class="brand__name">Brixwell<br>Capital</span></div>
  </div>

  <!-- open folder -->
  <div class="item folder-open">
    <div class="folder-open__panel folder-open__panel--left">
      <div class="folder-open__pocket"></div>
    </div>
    <div class="folder-open__panel folder-open__panel--right">
      <div class="folder-open__pocket">
        <div class="brand brand--light"><span class="brand__dot"></span><span class="brand__name">Brixwell<br>Capital</span></div>
      </div>
    </div>
  </div>

</body>
</html>
```